Home Health Care Agency Needs a Website (Seeking a PSD)

We need a user friendly website for a Home Health Care Agency. Our service is for the elderly and disabled. Frequently the busy professional middle-aged married daughter will use the website to arrange in-home care for an aging parent. Therefore, our website is primarily geared towards middle-aged women. In-home care is typically 24 hours a day so, a feeling of trustworthiness and security should be effectively conveyed. (Seeking a PSD- however, if you also offer coding, please let us know the cost.)

Target Market(s)

Frequently the busy professional middle-aged married daughter (possibly out of state) will use the website to arrange in-home care for an aging parent.

Industry/Entity Type

Security

Requirements
Must have
• Website must be clean, uncluttered and professional. The following menu pages are requested: Home, About Us, Services, Resources, FAQ, Employment & Contact.
Should not have
• Must not be too whimsical.

```html
<!DOCTYPE html>
<html lang="en">
<head>
<meta charset="utf-8">
<title>Willow Home Health</title>
<link href="https://fonts.googleapis.com/css2?family=Open+Sans:ital,wght@0,400;0,600;1,400&display=swap" rel="stylesheet">
<style>
:root{
  --brand:#2ab3dc;
  --navy:#3b4b6b;
  --ink:#333;
  --nav:#555;
  --quote-bg:#dfe3e8;
  --teal:#0a93a0;
  --yellow:#f2ee1a;
  --rule:#dcdcdc;
  --muted:#888;
}
*{box-sizing:border-box;margin:0;padding:0}
html,body{width:1200px;height:1015px;overflow:hidden;background:#fff;font-family:"Open Sans",sans-serif;color:var(--ink)}
.site-header{position:relative;height:100px}
.brand{position:absolute;left:111px;top:28px;display:flex;align-items:center;gap:8px;color:var(--brand);font-size:30px;font-weight:600;letter-spacing:-.5px}
.brand-mark{width:22px;height:22px;border-radius:50%;background:var(--brand)}
.search{position:absolute;left:939px;top:10px;width:151px;height:23px;border:1px solid #999;display:flex}
.search span{flex:1;font-size:12px;color:#777;padding:3px 5px}
.search b{width:20px;background:#555;display:flex;align-items:center;justify-content:center}
.main-nav{position:absolute;top:64px;left:0;width:1200px;font-size:16px;color:var(--nav)}
.main-nav a{position:absolute;color:inherit;text-decoration:none}
.main-nav a.active{color:var(--brand);font-weight:600;border-bottom:3px solid var(--brand);padding:0 4px 1px;margin-left:-4px}
.hero{position:absolute;top:100px;left:0;width:1200px;height:383px;background:var(--navy)}
.hero-photo{position:absolute;left:108px;top:0;width:985px;height:383px;background:linear-gradient(100deg,#d9cfc6 0%,#a88472 35%,#8a5d4c 55%,#d7c6bd 80%,#ece6e2 100%)}
.hero-caption{position:absolute;left:493px;top:284px;width:492px;height:89px;background:rgba(80,95,125,.82);color:#fff;padding:8px 14px;font-size:15.5px;line-height:20px;text-align:justify}
.hero-caption a{display:block;text-align:right;color:var(--yellow);font-weight:600;margin-top:10px}
.dots{position:absolute;left:9px;top:362px;display:flex;gap:4px}
.dots i{width:11px;height:11px;border:1px solid #fff;background:rgba(255,255,255,.5)}
.dots i:first-child{background:#444}
.testimonial{position:absolute;top:483px;left:0;width:1200px;height:88px;background:var(--quote-bg);padding:6px 111px 0 117px;font-size:14.6px;line-height:25px}
.testimonial cite{display:block;color:var(--muted);font-size:14.6px}
.services{position:absolute;left:111px;top:593px;width:568px}
.services h2{font-weight:400;font-size:21px;color:var(--navy);margin-bottom:2px}
.services p{font-size:14.6px;line-height:24.8px;text-align:justify}
.services ul{list-style:none;margin-top:10px}
.services li{font-size:14.6px;line-height:24.8px;padding-left:24px;position:relative}
.services li::before{content:"";position:absolute;left:4px;top:9px;width:9px;height:9px;background:#333}
.finder{position:absolute;left:738px;top:584px;width:355px;height:265px;background:var(--teal);color:#fff;text-align:center}
.finder-map{position:absolute;left:40px;top:55px;width:300px;height:165px;background:rgba(255,255,255,.07);border-radius:40px 60px 30px 50px}
.finder h3{position:relative;font-weight:400;font-size:21px;line-height:25px;margin-top:12px}
.finder label{position:relative;display:block;color:var(--yellow);font-size:17px;margin-top:30px}
.zip{position:relative;margin:6px auto 0;width:190px;height:30px;border:1px solid #fff;display:flex}
.zip b{margin-left:auto;width:24px;background:#fff;display:flex;align-items:center;justify-content:center}
.finder p{position:absolute;bottom:10px;left:0;width:100%;font-size:15.5px}
.finder p a{color:var(--yellow)}
.site-footer{position:absolute;left:108px;top:949px;width:985px;border-top:1px solid var(--rule);height:66px}
.social{position:absolute;left:14px;top:29px;display:flex;gap:8px}
.social i{width:22px;height:22px;border-radius:50%;background:#e3e3e3}
.footer-nav a{position:absolute;top:29px;font-size:12.5px;color:#555}
</style>
</head>
<body>
<header class="site-header">
  <div class="brand"><span class="brand-mark"></span>Willow Home Health</div>
  <div class="search"><span>Type here to find...</span><b><svg width="6" height="10"><path d="M0 0L6 5L0 10Z" fill="#fff"/></svg></b></div>
  <nav class="main-nav">
    <a class="active" href="#" style="left:399px">Home</a>
    <a href="#" style="left:485px">About Us</a>
    <a href="#" style="left:591px">Services</a>
    <a href="#" style="left:684px">Resources</a>
    <a href="#" style="left:787px">FAQ</a>
    <a href="#" style="left:862px">Employment</a>
    <a href="#" style="left:1000px">Contact Us</a>
  </nav>
</header>

<section class="hero">
  <div class="hero-photo" role="img" aria-label="Photo of an elderly woman and her caregiver sharing a warm moment">
    <div class="dots"><i></i><i></i><i></i></div>
    <div class="hero-caption">Lorem ipsum dolor sit amet, consectetur adipiscingly elit. Maecenas cursus, felis vitae ipsum.<a href="#">PELLENTESQUE ORNARE &gt;&gt;</a></div>
  </div>
</section>

<blockquote class="testimonial">
  <strong>&ldquo;</strong> Lorem ipsum dolor sit amet, consectetur adipiscing elit. Maecenas cursus, felis vitae tincidunt egestas, velit lorem tristique mi, a blandit neque mi ut ipsum. Aliquam vel tristique eros, et cursus risus. Cras elit diam, aliquet non sapien ac, pellentesque condimentum turpis.<strong>&rdquo;</strong>
  <cite>-- Nullam mi odio</cite>
</blockquote>

<section class="services">
  <h2>SERVICES</h2>
  <p>Lorem ipsum dolor sit amet, consectetur adipiscing elit. Maecenas cursus, felis vitae tincidunt egestas, velit lorem tristique mi, a blandit neque mi ut ipsum. Aliquam vel tristique eros, et cursus risus. Cras elit diam, aliquet non sapien ac, pellentesque condimentum turpis. Nullam mi odio, fermentum at ligula id, tincidunt gravida metus. Suspendisse potenti.</p>
  <ul>
    <li>Consectetur adipiscing elit.</li>
    <li>Maecenas cursus, felis vitae tincidunt egestas.</li>
    <li>Velit lorem tristique mi, a blandit neque mi ut ipsum.</li>
    <li>Aliquam vel tristique eros, et cursus risus.</li>
    <li>Cras elit diami.</li>
  </ul>
</section>

<aside class="finder">
  <div class="finder-map" role="img" aria-label="Faint map of the United States"></div>
  <h3>Find a caregiver for your<br>LOVED ONES...</h3>
  <label>Enter Zipcode</label>
  <div class="zip"><b><svg width="6" height="10"><path d="M0 0L6 5L0 10Z" fill="#0a93a0"/></svg></b></div>
  <p>Schedule a <a href="#">free consultation</a> with our experts</p>
</aside>

<footer class="site-footer">
  <div class="social"><i></i><i></i><i></i></div>
  <nav class="footer-nav">
    <a href="#" style="left:603px">Lorem ipsum</a>
    <a href="#" style="left:705px">Sit decor</a>
    <a href="#" style="left:777px">Gravida</a>
    <a href="#" style="left:852px">Metus</a>
    <a href="#" style="left:927px">Tincidunt</a>
  </nav>
</footer>
</body>
</html>
```